Medical Education and Learning Portal refresh

We at Vantrel Limited have developed a learning platform for medical students. It is based around multiple choice questions, but has social and gaming elements built in to make it fun. It will be used on desktop and mobile devices.

I am looking for a refresh of the 'dated' design into something modern and transferrable between devices.

Note that I have a 'focus group' of Medical Students on 4 February where the Top 3-4 designs will be shown to them for them to pick the winner.

I have also uploaded screenshots of the current site. Essentially I would like to reduce the complexity of design into 2-3 pages (currently unlogged in front/home page, logged in page with options, answer questions page, competition page, revision page/summary pages etc). What I am really after is a good clean colour scheme & structure.

If we get the design colour scheme right then I can pay additionally for coding and maybe some additional structure to pages.
Updates

Target Market(s)

Healthcare/Medical Students

Industry/Entity Type

Healthcare

Number of Pages Required

4 page

Font styles to use
Serif
Sans Serif

Requirements
Must have
• 'Clean' Web 2.0 (or later) feel to it.
• I also expect that the images for the trophies are 'cleaned up (each trophy has a bronze/silver/platinum version as users increase their score. I am looking for these to be clean and simple but fun!
• I also need the final design to be transferrable from a desktop browser to a mobile device. I will need designs for home page/content page/Q&A page.
• I previously had a side panel float over the site but that is dated now and I would like to have a page with each element clearly on it and any information would briefly float over this but not take the focus away from the main function of the page.
• I have included the 'bronze', 'silver', 'gold' trophy icons in the files. These are fine in one sense but ideally the colours will blend well too ...
• The following article summarises my must haves:
• http://plumquarry-notes.example/web-design/layout-trend-field-guide/
Nice to have
• Creative concept for presenting MCQ's to students, with a timer and box of information about the question (level of the question, the percent of student who get it right ... etc).
Should not have
• Too much complexity ... clean with a few colours is what I am after
• Note too that my logo is not changing and the colours should blend with this.

```html
<!DOCTYPE html>
<html lang="en">
<head>
<meta charset="utf-8">
<title>Vantrel — Medical Learning Portal</title>
<link rel="stylesheet" href="https://fonts.googleapis.com/css2?family=Open+Sans:ital,wght@0,400;0,600;0,700;1,400;1,600&display=swap">
<style>
:root{
  --blue:#4a6f96;
  --blue-dark:#3f6992;
  --orange:#fd9c0f;
  --ink:#2b2b2b;
  --body:#666;
  --muted:#a0a0a0;
  --footer:#252525;
  --white:#fff;
}
*{box-sizing:border-box;margin:0;padding:0}
html,body{width:1200px;height:2289px;overflow:hidden;background:var(--white)}
body{position:relative;font-family:"Open Sans",Arial,sans-serif;color:var(--ink)}
.abs{position:absolute}

/* header */
.site-header{left:0;top:0;width:1200px;height:60px;background:var(--white)}
.brand{left:251px;top:10px;display:flex;align-items:center;gap:8px;font-size:30px;font-weight:600;color:var(--blue);line-height:40px}
.brand-dot{width:12px;height:12px;border-radius:50%;background:var(--orange)}
.main-nav{top:23px;left:531px;font-size:8px;color:var(--blue);text-transform:uppercase}
.main-nav a{position:absolute;white-space:nowrap;color:inherit;text-decoration:none}
.main-nav a.accent{color:var(--orange)}
.main-nav .sep{position:absolute;left:329px;top:1px;width:1px;height:10px;background:#ddd}

/* hero */
.hero{left:0;top:60px;width:1200px;height:420px;
  background:linear-gradient(100deg,#6f8766 0%,#8c9886 18%,#b9bdbf 38%,#d7d9da 55%,#e6e7e8 75%,#cfd1d3 100%)}
.hero-title{left:0;top:134px;width:1212px;text-align:center;color:var(--white);font-size:30px;font-weight:700;letter-spacing:.3px}
.btn-start{left:527px;top:199px;width:146px;height:34px;border-radius:9px;background:var(--orange);color:var(--white);font-size:14px;font-weight:700;letter-spacing:1.5px;text-align:center;line-height:34px}
.hero-arrow{top:188px;width:45px;height:45px;border-radius:50%;background:#1e1e1e}
.hero-arrow svg{display:block}
.hero-dots{left:570px;top:394px;display:flex;gap:12px}

/* section headings */
.section-head{left:0;width:1200px;display:flex;align-items:center}
.section-head .rule{flex:1;height:2px;background:var(--orange)}
.section-head h2{font-weight:400;color:var(--blue-dark);font-size:30px;letter-spacing:1.5px;line-height:36px}
.section-sub{left:0;width:1200px;text-align:center;font-style:italic;font-size:11px;color:var(--muted);letter-spacing:.5px}

/* plans */
.plan{top:650px;width:230px;text-align:center}
.plan h3{font-size:15px;font-weight:400;color:var(--ink)}
.plan .btn-plan{display:block;margin:20px auto 0;width:146px;height:34px;border-radius:9px;background:var(--blue);color:var(--white);font-size:9.5px;font-weight:600;line-height:34px}
.plan-divider{top:638px;width:1px;height:120px;background:var(--orange);opacity:.6}
.btn-signup{left:518px;top:823px;width:160px;height:38px;border-radius:9px;background:var(--orange);color:var(--white);font-size:15px;font-weight:700;text-align:center;line-height:38px;letter-spacing:.5px}

/* news */
.article-photo{width:360px;height:267px}
.notch{position:absolute;top:112px;width:0;height:0;border-top:21px solid transparent;border-bottom:21px solid transparent}
.notch.left{right:0;border-right:18px solid var(--white)}
.notch.right{left:0;border-left:18px solid var(--white)}
.article-text{width:284px}
.article-text h3{font-size:19px;font-weight:400;color:#444;letter-spacing:.3px;line-height:24px}
.article-text .bar{width:56px;height:1px;background:#555;margin:17px 0 14px}
.article-text p{font-size:8.3px;line-height:14.4px;color:var(--body)}
.btn-read{display:block;margin-top:27px;width:89px;height:21px;border-radius:3px;background:var(--blue);color:var(--white);font-size:8.5px;font-weight:600;letter-spacing:.5px;text-align:center;line-height:21px}

/* about */
.about-text{left:259px;top:1945px;width:325px;height:286px;font-size:8.2px;line-height:14.4px;color:var(--body);overflow:hidden;
  -webkit-mask-image:linear-gradient(#000 82%,transparent);mask-image:linear-gradient(#000 82%,transparent)}
.about-divider{left:599px;top:1945px;width:2px;height:271px;background:#999}
.about-photo{left:644px;top:1947px;width:268px;height:264px;background:linear-gradient(160deg,#d9d4cc,#eeeeec 45%,#c9c3bd)}

/* footer */
.site-footer{left:0;top:2245px;width:1200px;height:44px;background:var(--footer);border-top:2px solid #3d5570}
.site-footer .copy{position:absolute;left:254px;top:20px;font-size:7px;color:#888}
.footer-nav a{position:absolute;top:19px;font-size:7.5px;color:#999;text-decoration:none;white-space:nowrap}
.social{position:absolute;top:20px;width:9px;height:9px;border-radius:50%;background:#bbb}
</style>
</head>
<body>

<header class="abs site-header">
  <div class="abs brand"><span class="brand-dot"></span>Vantrel</div>
  <nav class="abs main-nav">
    <a style="left:0">Home</a>
    <a style="left:48px">News</a>
    <a style="left:93px">Subscription Plans</a>
    <a style="left:203px">About Us</a>
    <a style="left:267px">Contact Us</a>
    <span class="sep"></span>
    <a class="accent" style="left:343px">Signup</a>
    <a class="accent" style="left:401px">Login</a>
  </nav>
</header>

<section class="abs hero" role="img" aria-label="Photo of a doctor in a white coat with a stethoscope holding a tablet">
  <h1 class="abs hero-title">TEST YOUR KNOWLEDGE IN MEDICINE</h1>
  <div class="abs btn-start">START NOW</div>
  <div class="abs hero-arrow" style="left:98px">
    <svg width="45" height="45" viewBox="0 0 45 45"><path d="M26 12 L16 22.5 L26 33" fill="none" stroke="#fff" stroke-width="1.6"/></svg>
  </div>
  <div class="abs hero-arrow" style="left:1053px">
    <svg width="45" height="45" viewBox="0 0 45 45"><path d="M19 12 L29 22.5 L19 33" fill="none" stroke="#fff" stroke-width="1.6"/></svg>
  </div>
  <div class="abs hero-dots">
    <svg width="12" height="12" viewBox="0 0 12 12"><path d="M6 1v10M1 6h10" stroke="#fff" stroke-width="3" opacity=".8"/></svg>
    <svg width="12" height="12" viewBox="0 0 12 12"><path d="M6 1v10M1 6h10" stroke="#fff" stroke-width="3"/></svg>
    <svg width="12" height="12" viewBox="0 0 12 12"><path d="M6 1v10M1 6h10" stroke="#fff" stroke-width="3" opacity=".8"/></svg>
  </div>
</section>

<div class="abs section-head" style="top:525px">
  <span class="rule"></span><h2 style="margin:0 62px">SUBSCRIPTION PLANS</h2><span class="rule"></span>
</div>
<p class="abs section-sub" style="top:565px">offers flexible subscription plans</p>

<div class="abs plan" style="left:241px"><h3>Regular Vantrel accaunt</h3><span class="btn-plan">FREE FOR 1000 MEMBERS</span></div>
<div class="abs plan-divider" style="left:470px"></div>
<div class="abs plan" style="left:483px"><h3>Premium Vantrel accaunt</h3><span class="btn-plan">£ 5 PER MONTH</span></div>
<div class="abs plan-divider" style="left:726px"></div>
<div class="abs plan" style="left:732px"><h3>Executive Vantrel accaunt</h3><span class="btn-plan">£ 10 PER MONTH</span></div>
<div class="abs btn-signup">SIG UP NOW</div>

<div class="abs section-head" style="top:936px">
  <span class="rule"></span><h2 style="margin:0 62px">NEWS</h2><span class="rule"></span>
</div>
<p class="abs section-sub" style="top:976px">what your peers say</p>

<div class="abs article-photo" style="left:244px;top:1028px;background:linear-gradient(120deg,#d9dde2,#b7bec7 40%,#3b3f45 80%,#25282c)" role="img" aria-label="Photo of a doctor reviewing brain scans at a computer workstation"><span class="notch left"></span></div>
<div class="abs article-text" style="left:637px;top:1070px">
  <h3>ARTICLE TITILE</h3><div class="bar"></div>
  <p>Lorem Ipsum is simply dummy text of the printing and typesetting industry. Lorem Ipsum has been the industry's standard dummy text ever since the 1500s, when an unknown printer took a galley of type and scrambled it to make a type specimen book. It has survived not only five centuries, but also the leap into electronic typesetting, remaining essentially unchanged. It was popularised in</p>
  <span class="btn-read">READ MORE</span>
</div>

<div class="abs article-text" style="left:277px;top:1343px">
  <h3>ARTICLE TITILE</h3><div class="bar"></div>
  <p>Lorem Ipsum is simply dummy text of the printing and typesetting industry. Lorem Ipsum has been the industry's standard dummy text ever since the 1500s, when an unknown printer took a galley of type and scrambled it to make a type specimen book. It has survived not only five centuries, but also the leap into electronic typesetting, remaining essentially unchanged. It was popularised in</p>
  <span class="btn-read" style="margin-left:-2px">READ MORE</span>
</div>
<div class="abs article-photo" style="left:604px;top:1296px;width:361px;background:linear-gradient(135deg,#e9e9ea,#d9dadc 45%,#eeeeef 70%,#5b6f95)" role="img" aria-label="Photo of a doctor and a student reviewing printed medical results at a desk"><span class="notch right"></span></div>

<div class="abs article-photo" style="left:244px;top:1563px;background:linear-gradient(135deg,#6b5a4e,#c7a792 40%,#efc9a8 70%,#e6d0c0)" role="img" aria-label="Photo of hands practising chest compressions on a training mannequin"><span class="notch left"></span></div>
<div class="abs article-text" style="left:637px;top:1610px">
  <h3>ARTICLE TITILE</h3><div class="bar"></div>
  <p>Lorem Ipsum is simply dummy text of the printing and typesetting industry. Lorem Ipsum has been the industry's standard dummy text ever since the 1500s, when an unknown printer took a galley of type and scrambled it to make a type specimen book. It has survived not only five centuries, but also the leap into electronic typesetting, remaining essentially unchanged. It was popularised in</p>
  <span class="btn-read">READ MORE</span>
</div>

<div class="abs section-head" style="top:1873px">
  <span class="rule"></span><h2 style="margin:0 62px">ABOUT US</h2><span class="rule"></span>
</div>

<p class="abs about-text">Lorem Ipsum is simply dummy text of the printing and typesetting industry. Lorem Ipsum has been the industry's standard dummy text ever since the 1500s, when an unknown printer took a galley of type and scrambled it to make a type specimen book. It has survived not only five centuries, but also the leap into electronic typesetting, remaining essentially unchanged. It was popularised in the 1960s with the release of transfer sheets containing Lorem Ipsum passages, and more recently with desktop layout tools including versions of Lorem Ipsum. Lorem Ipsum is simply dummy text of the printing and typesetting industry. Lorem Ipsum has been the industry's standard dummy text ever since the 1500s, when an unknown printer took a galley of type and scrambled it to make a type specimen book. It has survived not only five centuries, but also the leap into electronic typesetting, remaining essentially unchanged. It was popularised in the 1960s with the release of transfer sheets containing Lorem Ipsum passages, and more recently with desktop layout tools including versions of Lorem Ipsum. Lorem Ipsum is simply dummy text of the printing and typesetting industry. Lorem Ipsum has been the industry's standard dummy text ever since the 1500s, when an unknown printer took a galley of type and scrambled it to make a type specimen book. It has survived not only five centuries, but also the leap into electronic typesetting.</p>
<div class="abs about-divider"></div>
<div class="abs about-photo" role="img" aria-label="Group photo of medical students in white coats"></div>

<footer class="abs site-footer">
  <span class="copy">© 2015 - Copyright</span>
  <nav class="footer-nav">
    <a style="left:348px">HOME</a>
    <a style="left:391px">NEWS</a>
    <a style="left:434px">SUBSCRIPTION PLANS</a>
    <a style="left:536px">ABOUT US</a>
    <a style="left:595px">CONTACT US</a>
    <a style="left:666px">SIGNUP</a>
    <a style="left:719px">LOGIN</a>
  </nav>
  <span class="social" style="left:841px" aria-label="Social link"></span>
  <span class="social" style="left:871px" aria-label="Social link"></span>
  <span class="social" style="left:900px" aria-label="Social link"></span>
</footer>

</body>
</html>
```